Vantrelo App Homepage Design making customers feel in control of their spend

Hi,
We need a App Homepage design with a UI similar to the attached mock up on an Quorix 4. The app is intended to put customers in control of their usage and spend on their fixed phone, broadband, mobile, gas and electricity.

Please fee free to propose improvements to the background images, icons, colours, etc.

Any questions please let me know.

Thanks
Bertram

Target Market(s)

Consumer customers

Industry/Entity Type

Internet

Font styles to use
Sans Serif

Colors
3276b5
0255a3
85acd3
cfdeed
ffffff

Requirements
Must have
• Content in line with the guidelines in the attached mock up

```html
<!DOCTYPE html>
<html lang="en">
<head>
<meta charset="utf-8">
<title>Vantrelo – Home</title>
<link rel="stylesheet" href="https://fonts.googleapis.com/css2?family=Raleway:wght@300;400;500;600;700&display=swap">
<style>
  :root {
    --ink-dark: #1a0c04;
    --track: rgba(30, 14, 4, 0.88);
    --track-edge: #e0661c;
    --white: #ffffff;
    --soft-orange: #ffc58f;
    --brand-blue: #1d3c8f;
    --bar-power: #d6127c;
    --bar-gas: #e8461c;
    --bar-broadband: #5d9cf4;
    --bar-mobile: #8aaa12;
    --bar-landline: #0e2a6e;
    --icon-ring: #2a1306;
  }
  * { margin: 0; padding: 0; box-sizing: border-box; }
  html, body { width: 831px; height: 1200px; overflow: hidden; }
  body {
    font-family: "Raleway", sans-serif;
    color: var(--white);
    position: relative;
    background:
      radial-gradient(ellipse 520px 140px at 560px 1020px, rgba(255, 170, 100, 0.55), transparent 70%),
      radial-gradient(ellipse 600px 160px at 480px 700px, rgba(255, 140, 60, 0.45), transparent 70%),
      linear-gradient(178deg, rgba(40, 16, 4, 0.75) 0%, rgba(120, 44, 6, 0.3) 22%, transparent 40%),
      linear-gradient(90deg, rgba(60, 22, 4, 0.55) 0%, transparent 25%, transparent 75%, rgba(60, 22, 4, 0.5) 100%),
      repeating-linear-gradient(178deg, rgba(90, 30, 4, 0.18) 0 24px, transparent 24px 70px),
      linear-gradient(180deg, #c8560e 0%, #d86414 35%, #e0701c 60%, #e05a12 85%, #c44a0c 100%);
  }
  .menu-button { position: absolute; left: 100px; top: 95px; width: 42px; height: 36px; }
  .menu-button span { display: block; height: 4px; background: var(--white); margin-bottom: 12px; border-radius: 1px; }

  .brand { position: absolute; left: 245px; top: 78px; display: flex; align-items: center; gap: 18px; }
  .brand-dot { width: 64px; height: 64px; border-radius: 50%; background: var(--brand-blue); }
  .brand-name { font-size: 62px; font-weight: 700; color: var(--brand-blue); letter-spacing: -1px; }

  .avatar {
    position: absolute; left: 202px; top: 256px; width: 106px; height: 106px; border-radius: 50%;
    border: 6px solid #0d5d5a;
    background: radial-gradient(circle at 50% 40%, #f0dccb 0%, #b89a86 55%, #6a5a52 100%);
  }
  .greeting { position: absolute; left: 334px; top: 270px; }
  .greeting-title { font-size: 34px; font-weight: 600; line-height: 1.1; }
  .greeting-sub { font-size: 22px; font-weight: 400; color: var(--soft-orange); margin-top: 12px; }

  .charges { position: absolute; left: 213px; width: 462px; top: 425px; display: flex; justify-content: space-between; align-items: baseline; }
  .charges-label { font-size: 26px; font-weight: 700; }
  .charges-total { font-size: 42px; font-weight: 300; }

  .usage { position: absolute; left: 171px; top: 531px; width: 530px; list-style: none; }
  .usage-row { display: flex; align-items: center; height: 64px; margin-bottom: 37px; }
  .usage-icon {
    width: 64px; height: 64px; border-radius: 50%; background: var(--icon-ring);
    display: flex; align-items: center; justify-content: center; flex-shrink: 0; margin-right: 12px;
  }
  .usage-track {
    flex: 1; height: 58px; background: var(--track); border: 2px solid var(--track-edge);
    padding: 11px 8px; border-left: none;
  }
  .usage-fill { height: 32px; }
  .fill-power { width: 204px; background: var(--bar-power); }
  .fill-gas { width: 349px; background: var(--bar-gas); }
  .fill-broadband { width: 112px; background: var(--bar-broadband); }
  .fill-mobile { width: 61px; background: var(--bar-mobile); }
  .fill-landline { width: 81px; background: var(--bar-landline); }

  .bill {
    position: absolute; left: 159px; top: 1056px; width: 541px; height: 121px;
    background: rgba(255, 200, 160, 0.22); padding: 14px 28px;
  }
  .bill-amount { font-size: 48px; font-weight: 300; line-height: 1.1; }
  .bill-meta { font-size: 24px; font-weight: 400; margin-top: 4px; color: #ffe4cc; display: flex; gap: 28px; }
</style>
</head>
<body>
  <div class="menu-button" aria-label="Menu"><span></span><span></span><span></span></div>

  <div class="brand">
    <div class="brand-dot"></div>
    <div class="brand-name">Vantrelo</div>
  </div>

  <div class="avatar" role="img" aria-label="Profile photo of the account holder"></div>
  <div class="greeting">
    <p class="greeting-title">Good morning Sophie</p>
    <p class="greeting-sub">Welcome to Vantrelo</p>
  </div>

  <div class="charges">
    <span class="charges-label">Your&nbsp; Current Charges</span>
    <span class="charges-total">£63.99</span>
  </div>

  <ul class="usage">
    <li class="usage-row">
      <div class="usage-icon">
        <svg width="34" height="38" viewBox="0 0 34 38" fill="none" stroke="#c23fa0" stroke-width="2.5"><path d="M17 3a11 11 0 0 0-7 19.5c1.5 1.3 2 3 2 5h10c0-2 .5-3.7 2-5A11 11 0 0 0 17 3z"/><path d="M12 31h10M13 35h8"/></svg>
      </div>
      <div class="usage-track"><div class="usage-fill fill-power"></div></div>
    </li>
    <li class="usage-row">
      <div class="usage-icon">
        <svg width="40" height="36" viewBox="0 0 40 36" fill="#ef5a20"><path d="M8 12h22a2 2 0 0 1 2 2v2c0 6-5 10-13 10S6 22 6 16v-2a2 2 0 0 1 2-2z"/><path d="M32 15c4 0 6-3 6-3l-1 4c-1 2-3 3-5 3z"/><rect x="16" y="7" width="6" height="4" rx="2"/><g fill="#ffd2b0"><circle cx="10" cy="32" r="1.3"/><circle cx="14" cy="32" r="1.3"/><circle cx="18" cy="32" r="1.3"/><circle cx="22" cy="32" r="1.3"/><circle cx="26" cy="32" r="1.3"/></g></svg>
      </div>
      <div class="usage-track"><div class="usage-fill fill-gas"></div></div>
    </li>
    <li class="usage-row">
      <div class="usage-icon">
        <svg width="36" height="30" viewBox="0 0 36 30" fill="none" stroke="#6aa6f4" stroke-width="3" stroke-linecap="round"><path d="M3 11a21 21 0 0 1 30 0"/><path d="M8 16a14 14 0 0 1 20 0"/><path d="M13 21a7 7 0 0 1 10 0"/><circle cx="18" cy="26" r="1.8" fill="#6aa6f4"/></svg>
      </div>
      <div class="usage-track"><div class="usage-fill fill-broadband"></div></div>
    </li>
    <li class="usage-row">
      <div class="usage-icon">
        <svg width="24" height="38" viewBox="0 0 24 38" fill="none" stroke="#9ab818" stroke-width="2.5"><rect x="3" y="2" width="18" height="34" rx="3"/><path d="M3 8h18M3 29h18"/></svg>
      </div>
      <div class="usage-track"><div class="usage-fill fill-mobile"></div></div>
    </li>
    <li class="usage-row">
      <div class="usage-icon">
        <svg width="34" height="34" viewBox="0 0 34 34" fill="#1e4aa0"><path d="M6 30c-2-2-3-6 0-12C10 10 18 4 26 3c2 0 3 1 3 2l-1 4c0 1-1 2-2 2h-4c-4 2-8 6-10 11v4c0 1-1 2-2 2l-3 2z"/></svg>
      </div>
      <div class="usage-track"><div class="usage-fill fill-landline"></div></div>
    </li>
  </ul>

  <section class="bill">
    <p class="bill-amount">Latest bill : £123.99</p>
    <p class="bill-meta"><span>9 Dec 2016</span><span>Allowance renews in 18 days</span></p>
  </section>
</body>
</html>
```